TIDAL VERGE needs bisness cards pronto

Bisness name is "TIDAL VERGE" new bisness the bisness includes lawn mowing, garden matanace, and any jobs around the house.
I need a card that is colorful and vibrant and the bisness of lawn mowing maybe with some nature with it. It also needs my contact details"Darren Quellby mobile 0413562049 call for free quote and email norma.vance@fernmail.com.au and a catchy tag line

Industry/Entity Type

House

Requirements
Must have
• Bisness name "TIDAL VERGE"
Contact details "0413562049"
Email norma.vance@fernmail.com.au
Call for free quote

```html
<!DOCTYPE html>
<html lang="en">
<head>
<meta charset="utf-8">
<title>Tidal Verge – Business Card</title>
<link rel="stylesheet" href="https://fonts.googleapis.com/css2?family=Arimo:wght@700&family=Questrial&display=swap">
<style>
  :root {
    --lawn-light: #92cc3f;
    --lawn-mid: #78b936;
    --lawn-dark: #3f8a2a;
    --ink-green: #1b5e28;
    --panel-tint: rgba(255, 255, 255, 0.28);
    --blade-tint: rgba(255, 255, 255, 0.12);
    --paper: #ffffff;
  }
  html, body {
    margin: 0;
    padding: 0;
    width: 1200px;
    height: 720px;
    overflow: hidden;
    background: var(--paper);
  }
  .card {
    position: relative;
    width: 1200px;
    height: 720px;
    background: var(--paper);
    overflow: hidden;
  }
  .lawn-field {
    position: absolute;
    left: 0;
    top: 0;
    width: 1200px;
    height: 627px;
    background:
      radial-gradient(ellipse 62% 70% at 40% 38%, var(--lawn-light) 0%, var(--lawn-mid) 55%, var(--lawn-dark) 100%);
  }
  .grass-backdrop {
    position: absolute;
    left: 64px;
    top: 300px;
    width: 560px;
    height: 327px;
    background: linear-gradient(to top, var(--blade-tint), rgba(255, 255, 255, 0));
  }
  .business-name {
    position: absolute;
    left: 76px;
    top: 70px;
    margin: 0;
    font-family: "Arimo", Arial, sans-serif;
    font-weight: 700;
    font-size: 80px;
    letter-spacing: -2px;
    color: var(--paper);
    line-height: 1;
    white-space: nowrap;
  }
  .owner-name {
    position: absolute;
    right: 91px;
    top: 150px;
    margin: 0;
    font-family: "Questrial", sans-serif;
    font-size: 49px;
    color: var(--ink-green);
    line-height: 1;
  }
  .contact-panel {
    position: absolute;
    left: 313px;
    top: 208px;
    width: 940px;
    height: 189px;
    border-radius: 22px;
    background: var(--panel-tint);
  }
  .contact-line {
    position: absolute;
    right: 85px;
    margin: 0;
    font-family: "Questrial", sans-serif;
    font-size: 48px;
    color: var(--ink-green);
    line-height: 1;
    white-space: nowrap;
  }
  .contact-phone { top: 235px; }
  .contact-email { top: 320px; font-size: 46px; }
  .contact-label { margin-right: 20px; }
  .mower-art {
    position: absolute;
    left: 735px;
    top: 470px;
    width: 290px;
    height: 157px;
    background: linear-gradient(to bottom, rgba(255, 255, 255, 0.18), rgba(255, 255, 255, 0.6));
    border-radius: 70px 70px 0 0;
  }
  .verge-grass-art {
    position: absolute;
    left: 1025px;
    top: 590px;
    width: 175px;
    height: 37px;
    background: linear-gradient(to bottom, rgba(255, 255, 255, 0), rgba(255, 255, 255, 0.6));
  }
  .call-to-action {
    position: absolute;
    left: 80px;
    top: 566px;
    margin: 0;
    font-family: "Arimo", Arial, sans-serif;
    font-weight: 700;
    font-size: 72px;
    letter-spacing: -2.5px;
    color: var(--ink-green);
    line-height: 1;
    white-space: nowrap;
  }
</style>
</head>
<body>
  <main class="card">
    <div class="lawn-field"></div>
    <div class="grass-backdrop" role="img" aria-label="Faint tall grass blades rising from the bottom left"></div>

    <p class="business-name">TIDAL VERGE</p>

    <p class="owner-name">Darren Quellby</p>

    <div class="contact-panel"></div>
    <p class="contact-line contact-phone"><span class="contact-label">phone.</span>041.356.2049</p>
    <p class="contact-line contact-email">norma.vance@fernmail.com.au</p>

    <div class="mower-art" role="img" aria-label="White silhouette of a push lawn mower"></div>
    <div class="verge-grass-art" role="img" aria-label="White silhouette of a strip of grass tufts"></div>

    <p class="call-to-action">Call For Free Quote</p>
  </main>
</body>
</html>
```